Re-Design of Business Card for Marine Sales People

We are looking to Re-design our business cards to look like they are in the 21st century. We are a full service marina and sell a lot of new/used boats. May want a spot on the card for our 3 main brands we sell. A picture spot of the sales man would be nice, but not necessarily.

```html
<!DOCTYPE html>
<html lang="en">
<head>
<meta charset="utf-8">
<title>Harborline Marine – Business Card</title>
<link rel="stylesheet" href="https://fonts.googleapis.com/css2?family=Open+Sans:wght@400;600;700&display=swap">
<style>
  :root {
    --bg: #e9ecf0;
    --sky: #1b9fdc;
    --navy: #132d57;
    --white: #ffffff;
    --shadow: rgba(10, 25, 50, 0.18);
  }
  * { box-sizing: border-box; margin: 0; padding: 0; }
  html, body { width: 1200px; height: 780px; overflow: hidden; }
  body {
    background: var(--bg);
    font-family: "Open Sans", Arial, sans-serif;
    position: relative;
  }
  .card {
    position: absolute;
    top: 235px;
    width: 540px;
    height: 310px;
    border-radius: 22px;
    overflow: hidden;
    box-shadow: 0 14px 30px var(--shadow);
  }
  .card--front { left: 40px; background: var(--sky); }
  .card--back { left: 620px; background: var(--white); }

  .front-label {
    position: absolute;
    left: 55px; top: 110px;
    width: 430px; height: 90px;
    background: var(--white);
    border-radius: 20px;
    display: flex; align-items: center; justify-content: center; gap: 14px;
  }
  .brand-dot { width: 18px; height: 18px; border-radius: 50%; background: var(--sky); flex: none; }
  .brand-name {
    font-weight: 700; font-size: 28px; letter-spacing: 1px;
    color: var(--sky); text-transform: uppercase; white-space: nowrap;
  }

  .back-wave { position: absolute; inset: 0; width: 540px; height: 310px; }

  .back-label {
    position: absolute;
    right: 40px; top: 18px;
    width: 250px; height: 40px;
    background: var(--navy);
    border-radius: 12px;
    display: flex; align-items: center; justify-content: center; gap: 9px;
  }
  .back-label .brand-dot { width: 10px; height: 10px; background: var(--white); }
  .back-label .brand-name { font-size: 14px; letter-spacing: 0.5px; color: var(--white); }

  .contact {
    position: absolute;
    left: 38px; top: 154px;
    color: var(--white);
  }
  .contact__name { font-weight: 700; font-size: 22px; color: var(--sky); line-height: 1.1; }
  .contact__title { font-weight: 600; font-size: 13px; margin-top: 2px; }
  .contact__address { font-size: 11.5px; line-height: 1.4; margin-top: 8px; }
  .contact__list { list-style: none; margin-top: 6px; font-size: 11.5px; line-height: 1.55; }
  .contact__list li { display: flex; align-items: center; gap: 8px; }
  .icon { width: 12px; height: 12px; flex: none; }
</style>
</head>
<body>

<section class="card card--front" aria-label="Card front">
  <div class="front-label">
    <span class="brand-dot"></span>
    <span class="brand-name">Harborline Marine</span>
  </div>
</section>

<section class="card card--back" aria-label="Card back">
  <svg class="back-wave" viewBox="0 0 540 310" aria-hidden="true">
    <path fill="var(--navy)" d="M0 152 C140 110 300 104 400 92 C470 84 515 62 540 36 L540 310 L0 310 Z"/>
    <path fill="var(--sky)" d="M30 146 C160 102 310 90 410 80 C470 72 510 52 530 32 C505 62 465 80 405 88 C305 100 170 110 30 146 Z"/>
    <path fill="var(--sky)" d="M230 108 C320 98 420 90 470 78 C500 70 520 58 535 44 C515 64 485 76 440 84 C380 94 300 102 230 108 Z"/>
  </svg>

  <div class="back-label">
    <span class="brand-dot"></span>
    <span class="brand-name">Harborline Marine</span>
  </div>

  <div class="contact">
    <p class="contact__name">Mara Lindqvist</p>
    <p class="contact__title">Managing Director</p>
    <p class="contact__address">418 Shoreline Ave. Suite 120<br>Bayport, NH 03220</p>
    <ul class="contact__list">
      <li>
        <svg class="icon" viewBox="0 0 16 16"><path fill="var(--sky)" d="M3.5 1 6 3.5 4.6 5.2c.9 2 2.3 3.4 4.2 4.2L10.5 8 13 10.5 11.8 13C7 13 3 9 3 4.2Z"/></svg>
        (603) 555-0147
      </li>
      <li>
        <svg class="icon" viewBox="0 0 16 16"><rect x="1.5" y="3.5" width="13" height="9" rx="1.5" fill="var(--sky)"/><path d="M2 4.5 8 9l6-4.5" stroke="var(--navy)" stroke-width="1.2" fill="none"/></svg>
        info@harborlinemarine.com
      </li>
      <li>
        <svg class="icon" viewBox="0 0 16 16"><circle cx="8" cy="8" r="6.5" fill="var(--sky)"/><path d="M1.5 8h13M8 1.5c-3 3.5-3 9.5 0 13M8 1.5c3 3.5 3 9.5 0 13" stroke="var(--navy)" stroke-width="1" fill="none"/></svg>
        www.harborlinemarine.com
      </li>
    </ul>
  </div>
</section>

</body>
</html>
```